Townhome Multi-Family Property Exterior Sign

Hello. We are looking for a new design for our exterior pylon for for a multi-family housing property in Texas. The design will need to go on a new sign panel to replace the existing (see photo of existing). We are looking to see both modern and contemporary designs. Included the sign should be the name, Loma Brisa Townhomes and the web address www.lomabrisatownhomes.example.

Attached here is a PDF file of the proposed new sign shape. We are open to other shape ideas as well if your design would better suit a more rectangular shape.

Industry/Entity Type

Property

Font styles to use
Serif
Sans Serif

Colors
9bcb3c

Requirements
Must have
• Name of building: Loma Brisa Townhomes
• Website: www.lomabrisatownhomes.example
Nice to have
• Address: 420-530 Halvorsen Lane (only if it fits nicely)

```html
<!DOCTYPE html>
<html lang="en">
<head>
<meta charset="utf-8">
<title>Loma Brisa Townhomes – Exterior Sign</title>
<link rel="stylesheet" href="https://fonts.googleapis.com/css2?family=Josefin+Sans:wght@400&family=Montserrat:wght@600;700&display=swap">
<style>
  :root {
    --backdrop: #e8e8e8;
    --leaf: #8dc63f;
    --leaf-deep: #7fb735;
    --cream: #f7f8e6;
    --cream-edge: #e9f0c8;
    --ink: #231f20;
    --post: #2b2b2b;
  }
  * { margin: 0; padding: 0; box-sizing: border-box; }
  html, body { width: 1200px; height: 715px; overflow: hidden; }
  body { background: var(--backdrop); position: relative; }

  .sign-post { position: absolute; top: 90px; width: 44px; height: 498px; background: var(--post); }
  .sign-post--left { left: 128px; }
  .sign-post--right { left: 1056px; }
  .post-cap { position: absolute; top: -20px; left: -10px; width: 64px; height: 24px; }

  .sign-panel {
    position: absolute; left: 172px; top: 130px; width: 884px; height: 458px;
    background: var(--leaf); overflow: hidden;
    box-shadow: 0 14px 22px rgba(0,0,0,0.25);
  }
  .meadow-band {
    position: absolute; left: 0; top: 215px; width: 100%; height: 243px;
    background: linear-gradient(180deg, var(--cream) 0%, var(--cream) 45%, var(--cream-edge) 100%);
  }
  .hill { position: absolute; left: 0; top: 0; width: 884px; height: 458px; }

  .divider-ornament {
    position: absolute; left: 278px; top: 22px; width: 320px; height: 10px;
    background: var(--leaf-deep); border-radius: 5px;
  }
  .name-top, .name-main, .address, .web {
    position: absolute; left: 0; width: 100%; text-align: center; color: var(--ink); white-space: nowrap;
  }
  .name-top {
    top: 38px; font-family: "Josefin Sans", sans-serif; font-size: 48px; letter-spacing: 2px; line-height: 1;
  }
  .name-main {
    top: 88px; font-family: "Josefin Sans", sans-serif; font-size: 106px; letter-spacing: 2px; line-height: 1;
  }
  .pin-icon { position: absolute; left: 426px; top: 220px; width: 32px; height: 40px; }
  .address {
    top: 266px; font-family: "Montserrat", sans-serif; font-weight: 700; font-size: 48px; line-height: 1; letter-spacing: 0.5px;
  }
  .web {
    top: 394px; font-family: "Montserrat", sans-serif; font-weight: 600; font-size: 34px; line-height: 1;
  }
</style>
</head>
<body>
  <div class="sign-post sign-post--left">
    <svg class="post-cap" viewBox="0 0 64 24"><polygon points="10,0 54,0 64,24 0,24" fill="#2b2b2b"/></svg>
  </div>
  <div class="sign-post sign-post--right">
    <svg class="post-cap" viewBox="0 0 64 24"><polygon points="10,0 54,0 64,24 0,24" fill="#2b2b2b"/></svg>
  </div>

  <div class="sign-panel">
    <div class="meadow-band" role="img" aria-label="Soft grass meadow backdrop"></div>
    <svg class="hill" viewBox="0 0 884 458" aria-hidden="true">
      <path d="M0 430 Q 300 330 548 342 Q 760 352 884 380 L884 458 L0 458 Z" fill="var(--leaf)"/>
      <path d="M0 422 Q 300 322 548 334 Q 760 344 884 372" fill="none" stroke="var(--ink)" stroke-width="2"/>
    </svg>

    <div class="divider-ornament" role="img" aria-label="Decorative scroll divider"></div>
    <div class="name-top">LOMA BRISA</div>
    <div class="name-main">TOWNHOMES</div>

    <svg class="pin-icon" viewBox="0 0 32 40" aria-hidden="true">
      <path d="M16 3 C9 3 5 8 5 14 C5 21 16 31 16 31 C16 31 27 21 27 14 C27 8 23 3 16 3 Z" fill="none" stroke="var(--ink)" stroke-width="2.4"/>
      <circle cx="16" cy="14" r="4" fill="none" stroke="var(--ink)" stroke-width="2.4"/>
      <path d="M4 31 L2 38 L30 38 L28 31" fill="none" stroke="var(--ink)" stroke-width="2.4"/>
    </svg>
    <div class="address">420-530 HALVORSEN LANE</div>
    <div class="web">www.lomabrisatownhomes.example</div>
  </div>
</body>
</html>
```